Mental Health Therapy Website

I need a design for a mental health therapy website. It is a private practice. The business name is Hale Wellspring, PLLC. My name is Martin Hale, LMHC, NCC, DCC. I would like some of the features/menus to be Home; Welcome/About Me, Rates and Services, Common Questions, and Contact.
If possible I would like a blog on the main page that I can update with articles I write. I would like the contact page to feature a map to my location (4316 Fernbrook Ave. S, Lakewood, WA 98421).
I would like to place a small photo of me on the Welcome/About page.
I am new to this so if I am forgetting anything, please ask me!!
I will upload my logo so you can fit it and the color scheme into the design.
Thank you so very much!

```html
<!DOCTYPE html>
<html lang="en">
<head>
<meta charset="utf-8">
<title>Hale Wellspring Counseling</title>
<link href="https://fonts.googleapis.com/css2?family=Cinzel:wght@400;700&family=Open+Sans:ital,wght@0,400;0,600;0,700;1,400&display=swap" rel="stylesheet">
<style>
:root{
  --blue:#1f5a9e;
  --blue-dark:#174a87;
  --green:#6a9f35;
  --green-light:#86b84a;
  --text:#666;
  --text-dark:#333;
  --page:#fdfdfd;
  --header:#efefef;
  --footer:#1f1f1f;
  --band:#f0f0f0;
}
*{box-sizing:border-box;margin:0;padding:0}
html,body{width:1024px;height:1200px;overflow:hidden}
body{position:relative;background:var(--page);font-family:"Open Sans",Arial,sans-serif;color:var(--text)}
.abs{position:absolute}
.display{font-family:"Cinzel",Georgia,serif}

.site-header{left:0;top:0;width:1024px;height:96px;background:var(--header);border-top:3px solid var(--blue)}
.brand{left:136px;top:20px;display:flex;align-items:center;gap:8px}
.brand-mark{width:44px;height:44px;border-radius:50%;background:var(--green)}
.brand-name{font-family:"Cinzel",Georgia,serif;font-size:25px;color:var(--blue);line-height:1}
.call{left:487px;top:36px;display:flex;align-items:center;gap:6px;font-size:14px;color:#888}
.call strong{color:var(--blue-dark);font-weight:600}
.call-icon{width:20px;height:20px;background:var(--blue);border-radius:3px;display:flex;align-items:center;justify-content:center}
.btn-appointment{left:712px;top:26px;width:177px;height:40px;background:linear-gradient(#3473b8,var(--blue-dark));color:#fff;font-family:"Cinzel",Georgia,serif;font-size:13.5px;font-weight:700;display:flex;align-items:center;justify-content:center;border-radius:2px;box-shadow:0 2px 3px rgba(0,0,0,.3)}

.main-nav{left:0;top:96px;width:1024px;height:41px;background:linear-gradient(var(--green-light),var(--green));display:flex;align-items:center;justify-content:center;gap:0}
.main-nav a{font-family:"Cinzel",Georgia,serif;color:#fff;text-decoration:none;font-size:13.5px;letter-spacing:.3px;padding:0 26px}

.hero{left:0;top:137px;width:1024px;height:364px;background:radial-gradient(ellipse at 35% 40%,#c8d86a 0%,#97ad3a 35%,#5d6e2a 70%,#3d3a2a 100%)}
.hero-panel{left:584px;top:253px;width:440px;height:140px;background:rgba(50,55,30,.6)}
.hero-title{left:627px;top:276px;font-family:"Cinzel",Georgia,serif;color:#fff;font-size:27px;line-height:31px;text-shadow:0 1px 2px rgba(0,0,0,.4)}
.hero-sub{left:630px;top:350px;color:#fff;font-size:12px;font-weight:700}
.hero-shadow{left:200px;top:501px;width:624px;height:30px;background:radial-gradient(ellipse at 50% 0%,rgba(0,0,0,.18),rgba(0,0,0,0) 70%)}

.section-title{font-family:"Cinzel",Georgia,serif;color:var(--blue);font-size:21px;font-weight:400;letter-spacing:.5px}
.portrait{left:131px;top:556px;width:116px;height:116px;border-radius:50%;background:linear-gradient(#e6e6e6,#bbb)}
.doc-name{left:120px;top:682px;width:142px;text-align:center;font-family:"Cinzel",Georgia,serif;color:var(--blue);font-size:14px}
.doc-role{left:120px;top:701px;width:142px;text-align:center;font-family:"Cinzel",Georgia,serif;color:var(--blue);font-size:10px}
.about-title{left:268px;top:550px}
.about-text{left:269px;top:596px;width:362px;font-size:13.5px;line-height:19px}
.about-text p+p{margin-top:19px}
.about-text b{color:#555}

.testi-title{left:648px;top:549px}
.testimonial{left:669px;width:230px;font-size:11px;line-height:16px;font-style:italic}
.testimonial .who{margin-top:10px;font-style:normal;color:var(--text-dark);font-size:11px}
.testimonial .who b{font-weight:700}
.testimonial .sep{color:#aaa;padding:0 5px}

.col{top:795px;width:240px}
.col .section-title{text-align:center}
.col .rule{height:4px;margin-top:15px;border-top:1px dotted #bbb;border-bottom:1px dotted #bbb}
.col .intro{margin-top:19px;font-size:13.5px;line-height:19px}
.col ul{list-style:none;margin-top:18px;font-size:13.5px}
.col li{height:25.6px;display:flex;align-items:center;gap:10px}
.col li::before{content:"";border-left:5px solid #777;border-top:4px solid transparent;border-bottom:4px solid transparent}
.col li b{font-weight:600;color:#555}

.news-item{left:647px;width:245px}
.news-title{font-family:"Cinzel",Georgia,serif;color:var(--green);font-size:11.5px;text-decoration:underline;padding-left:3px}
.news-body{display:flex;gap:14px;margin-top:6px}
.news-thumb{width:68px;height:58px;flex:none}
.news-text{font-size:9.5px;line-height:14.5px}
.news-date{margin-top:6px;font-size:8px;font-weight:700;color:#555}

.newsletter{left:0;top:1089px;width:1024px;height:71px;background:var(--band);border-top:1px solid #ddd}
.nl-title{left:129px;top:1108px;font-family:"Cinzel",Georgia,serif;color:var(--green);font-size:13.5px}
.nl-sub{left:129px;top:1126px;font-size:9.5px;color:#888}
.nl-input{left:346px;top:1109px;width:278px;height:31px;background:#fff;border:1px solid #ccc;font-size:10px;color:#999;padding:0 13px;display:flex;align-items:center}
.nl-submit{left:623px;top:1109px;width:88px;height:31px;background:linear-gradient(var(--green-light),var(--green));color:#fff;font-size:11.5px;font-weight:700;display:flex;align-items:center;justify-content:center}
.social{top:1111px;width:28px;height:28px;border-radius:3px;background:#4b6ea3}

.site-footer{left:0;top:1160px;width:1024px;height:40px;background:var(--footer);color:#999;font-size:10px}
.copyright{left:128px;top:14px}
.footer-links{right:127px;top:14px;display:flex;gap:10px}
.footer-links span.dot{color:#666}
</style>
</head>
<body>

<header class="site-header abs"></header>
<div class="brand abs"><span class="brand-mark"></span><span class="brand-name">Hale Wellspring</span></div>
<div class="call abs">
  <span class="call-icon"><svg width="12" height="12" viewBox="0 0 24 24"><path fill="#fff" d="M6.6 10.8a15.1 15.1 0 0 0 6.6 6.6l2.2-2.2c.3-.3.7-.4 1-.2 1.1.4 2.3.6 3.6.6.6 0 1 .4 1 1V20c0 .6-.4 1-1 1C10.6 21 3 13.4 3 4c0-.6.4-1 1-1h3.5c.6 0 1 .4 1 1 0 1.3.2 2.5.6 3.6.1.3 0 .7-.2 1z"/></svg></span>
  Call us today <strong>+1 800.555.0147</strong>
</div>
<div class="btn-appointment abs">Schedule Appointment</div>

<nav class="main-nav abs">
  <a href="#">Home</a><a href="#">About Me</a><a href="#">Rates and Services</a><a href="#">Common Questions</a><a href="#">Contact</a>
</nav>

<div class="hero abs" role="img" aria-label="Sunlit green leaves on a branch against a bright sky"></div>
<div class="hero-panel abs"></div>
<h1 class="hero-title abs" style="font-weight:400">You don’t have to<br>suffer any longer.</h1>
<p class="hero-sub abs">Let’s talk and take the next step toward healing.</p>
<div class="hero-shadow abs"></div>

<div class="portrait abs" role="img" aria-label="Portrait photo of the therapist"></div>
<div class="doc-name abs">Dr. Martin Hale</div>
<div class="doc-role abs">Psychologist</div>
<h2 class="section-title about-title abs">About Me</h2>
<div class="about-text abs">
  <p>I am a <b>trauma certified</b> therapist that utilizes CBT+ to assist with trauma.</p>
  <p>My approach to therapy is psychodynamic that utilizes tools from CBT, Solutions-focused, Emotions-focused, and Psych-oeducation therapies to assist clients managing depression, anxiety, truama, phobias, personality disorders, ADHD, self-injury,and communication issues.</p>
</div>

<h2 class="section-title testi-title abs">Client Testimonials</h2>
<div class="testimonial abs" style="top:594px">
  <p>“Lorem ipsum dolor sit amet, consectetur adipisicing elit, sed do eiusmod tempor incididunt ut labore et dolore magna aliqua.</p>
  <p class="who"><b>Clara Benn</b><span class="sep">|</span>Northfield Co.</p>
</div>
<div class="testimonial abs" style="top:685px">
  <p>“Lorem ipsum dolor sit amet, consectetur adipisicing elit, sed do eiusmod tempor incididunt ut labore et dolore magna aliqua.</p>
  <p class="who"><b>Clara Benn</b><span class="sep">|</span>Northfield Co.</p>
</div>

<section class="col abs" style="left:138px">
  <h2 class="section-title">Services</h2>
  <div class="rule"></div>
  <p class="intro">Lorem ipsum dolor sit amet, consecte-tur adipisicing elit, sed do eiusmod tempor incididunt ut labore et dolore.</p>
  <ul><li>Counselling</li><li>General Counselling</li><li>Trauma Therapy</li><li>Consultation</li></ul>
</section>
<section class="col abs" style="left:393px">
  <h2 class="section-title">Consultation Hours</h2>
  <div class="rule"></div>
  <p class="intro">Lorem ipsum dolor sit amet, consecte-tur adipisicing elit, sed do eiusmod tempor incididunt ut labore et dolore.</p>
  <ul><li><b>Monday - Friday</b></li><li><b>9:00 am - 6:00pm</b></li><li>Call us at: +1 800.555.0147</li><li>Email: info@halewellspring.com</li></ul>
</section>
<section class="col abs" style="left:649px">
  <h2 class="section-title">Latest News</h2>
  <div class="rule"></div>
</section>

<article class="news-item abs" style="top:857px">
  <div class="news-title">Trauma Therapy Can Help</div>
  <div class="news-body">
    <div class="news-thumb" role="img" aria-label="Person in a hooded jacket sitting by the sea" style="background:linear-gradient(#c9ccd0,#8a8f96)"></div>
    <div><p class="news-text">The point of using Lorem Ipsum is that it has a more-or-less normal distribution of letters, as opposed..</p><p class="news-date">▫ 8 December 2013</p></div>
  </div>
</article>
<article class="news-item abs" style="top:958px">
  <div class="news-title">5 Tips for Better Outlook in Life</div>
  <div class="news-body">
    <div class="news-thumb" role="img" aria-label="Misty lake with a wooden post" style="background:linear-gradient(#dfe6d8,#7d9460)"></div>
    <div><p class="news-text">The point of using Lorem Ipsum is that it has a more-or-less normal distribution of letters, as opposed..</p><p class="news-date">▫ 8 December 2013</p></div>
  </div>
</article>

<div class="newsletter abs"></div>
<div class="nl-title abs">Subscribe to our Newsletter</div>
<div class="nl-sub abs">Get the latest updates about mental health</div>
<div class="nl-input abs">Enter Your Email Address</div>
<div class="nl-submit abs">Submit</div>
<div class="social abs" style="left:760px" aria-label="Social link"></div>
<div class="social abs" style="left:797px" aria-label="Social link"></div>
<div class="social abs" style="left:833px" aria-label="Social link"></div>
<div class="social abs" style="left:868px" aria-label="Social link"></div>

<footer class="site-footer abs">
  <div class="copyright abs">Copyright © 2014 HaleWellspring All Rights Reserved.</div>
  <div class="footer-links abs"><span>Site Map</span><span class="dot">•</span><span>Privacy Policy</span><span class="dot">•</span><span>Contact Us</span></div>
</footer>

</body>
</html>
```